" Clínica médica que atua nas diversas especialidades e realiza atendimentos particulares a preços acessíveis, podendo futuramente atender planos de saúde. "

```html
<!DOCTYPE html>
<html lang="pt-BR">
<head>
<meta charset="UTF-8">
<title>ClinMais — Clínica Médica</title>
<link rel="stylesheet" href="https://fonts.googleapis.com/css2?family=Montserrat:wght@500;600;700;800&family=Open+Sans:wght@400;600&display=swap">
<style>
  :root {
    --page-bg: #e6e8ea;
    --navy: #1f3a52;
    --panel: #234a60;
    --teal: #2f8f8a;
    --green: #3fa37a;
    --white: #ffffff;
    --text-dark: #2c3e50;
    --text-muted: #7d8b96;
    --strip: #eef1f3;
    --photo-a: #dfe8ee;
    --photo-b: #b9ccd8;
  }
  * { box-sizing: border-box; margin: 0; padding: 0; }
  html, body { width: 1200px; height: 1200px; overflow: hidden; }
  body {
    background: var(--page-bg);
    font-family: "Open Sans", Arial, sans-serif;
    display: flex; align-items: center; justify-content: center;
  }
  .site {
    width: 1200px; height: 760px; background: var(--white);
    display: flex; flex-direction: column; overflow: hidden;
  }
  .topbar {
    height: 40px; background: var(--navy); color: #c9d5df;
    font-size: 13px; display: flex; align-items: center;
    padding: 0 60px; gap: 40px;
  }
  .topbar .contact-item { display: flex; align-items: center; gap: 8px; }
  .topbar .social { margin-left: auto; display: flex; gap: 12px; }
  .topbar .social span { width: 12px; height: 12px; border-radius: 50%; background: #8ea3b4; }
  .header {
    height: 110px; display: flex; align-items: center; padding: 0 60px;
  }
  .brand { display: flex; align-items: center; gap: 12px; }
  .brand-dot { width: 30px; height: 30px; background: var(--teal); border-radius: 4px; }
  .brand-name {
    font-family: "Montserrat", Arial, sans-serif; font-weight: 700;
    font-size: 34px; color: var(--teal);
  }
  .nav { margin-left: auto; display: flex; gap: 28px; list-style: none; }
  .nav li {
    font-family: "Montserrat", Arial, sans-serif; font-weight: 700;
    font-size: 13px; color: var(--text-dark); letter-spacing: .3px;
  }
  .nav li.active { color: var(--green); }
  .hero { position: relative; height: 480px; }
  .hero-photo {
    position: absolute; inset: 0;
    background: linear-gradient(100deg, var(--photo-a) 0%, var(--photo-b) 55%, #9fb6c6 100%);
  }
  .hero-panel { position: absolute; inset: 0; }
  .hero-copy {
    position: absolute; left: 700px; top: 90px; width: 440px; color: var(--white);
    font-family: "Montserrat", Arial, sans-serif; font-weight: 800;
  }
  .hero-title { font-size: 34px; line-height: 1.2; }
  .hero-sub { font-size: 34px; line-height: 1.2; margin-top: 40px; }
  .hero-button {
    display: inline-block; margin-top: 40px; background: var(--green);
    color: var(--white); font-family: "Open Sans", Arial, sans-serif;
    font-weight: 600; font-size: 14px; padding: 12px 32px;
  }
  .strip { flex: 1; background: var(--strip); }
</style>
</head>
<body>
  <main class="site">
    <div class="topbar">
      <div class="contact-item">
        <svg width="13" height="13" viewBox="0 0 24 24"><path fill="#c9d5df" d="M6.6 10.8a15.1 15.1 0 0 0 6.6 6.6l2.2-2.2c.3-.3.7-.4 1-.2 1.1.4 2.3.6 3.6.6.6 0 1 .4 1 1V20c0 .6-.4 1-1 1A17 17 0 0 1 3 4c0-.6.4-1 1-1h3.5c.6 0 1 .4 1 1 0 1.3.2 2.5.6 3.6.1.3 0 .7-.2 1z"/></svg>
        Tel: (11) 4002-1234
      </div>
      <div class="contact-item">Email: contato@clinmais.com.br</div>
      <div class="social"><span></span><span></span><span></span><span></span></div>
    </div>
    <header class="header">
      <div class="brand"><span class="brand-dot"></span><span class="brand-name">ClinMais</span></div>
      <ul class="nav">
        <li class="active">HOME</li>
        <li>QUEM SOMOS</li>
        <li>CONSULTAS E TRATAMENTOS</li>
        <li>EXAMES</li>
        <li>AGENDAMENTO</li>
        <li>FALE CONOSCO</li>
      </ul>
    </header>
    <section class="hero">
      <div class="hero-photo" role="img" aria-label="Foto de médicos sorridentes de jaleco atendendo pacientes na clínica"></div>
      <svg class="hero-panel" width="1200" height="480" viewBox="0 0 1200 480">
        <polygon points="640,0 1200,0 1200,480 560,480" fill="var(--panel)"/>
        <polygon points="640,0 660,0 580,480 560,480" fill="var(--teal)"/>
      </svg>
      <div class="hero-copy">
        <h1 class="hero-title">QUALIDADE &amp; SATISFAÇÃO GARANTIDA</h1>
        <h2 class="hero-sub">CONHEÇA NOSSAS ÁREAS DE ATUAÇÃO</h2>
        <span class="hero-button">Saiba mais</span>
      </div>
    </section>
    <div class="strip"></div>
  </main>
</body>
</html>
```